[WEB DESIGN - Start-up] Online LOANS against Luxury Assets - Needs a Web Design

Hello,
We need a web design for a new company. We make online LOANS against Luxury assets.
The name is private, that's why you could remplace it by the term "LOGO" or "ENTERPRISE".

In attachments, you'll find few models that we would like. Nonetheless, we don't want a copy of these screenshots. They are only prototypes that we made. Here we expect you to lead a professional web Design with your intuition and your ideas.

The final design should communicate start-up spirit, professionalism and fluidity.

Best Regards.

Industry/Entity Type

Finance

Number of Pages Required

2 page

Font styles to use
Sans Serif

Colors
f78f20
ffffff
b2b2b2
e9e9e9

Requirements
Must have
• The designer will draw on the 2015 web trends.
• The subject site is serious (loans against luxury assets), but the site should be modern and pleasant.
• PLEASE REFER YOU TO MY MODEL ( ATTACHMENTS)
Nice to have
• Surprise-me ! Welcome to a lot of imagination.

```html
<!DOCTYPE html>
<html lang="fr">
<head>
<meta charset="utf-8">
<title>LOGO – Prêts contre biens de luxe</title>
<link rel="stylesheet" href="https://fonts.googleapis.com/css2?family=Open+Sans:wght@400;600;700;800&display=swap">
<style>
:root{
  --orange:#f78f20;
  --white:#ffffff;
  --grey:#b2b2b2;
  --light:#e9e9e9;
  --dark:#1e1e1e;
  --text:#555;
}
*{box-sizing:border-box;margin:0;padding:0}
html,body{width:695px;height:1200px;overflow:hidden}
body{font-family:"Open Sans",Arial,sans-serif;color:var(--text);background:var(--white);font-size:6px;line-height:1.45}
.hero{position:relative;height:262px;background:linear-gradient(180deg,#3a342e 0%,#5a5046 45%,#2c2824 100%);}
.hero-photo{position:absolute;inset:0;background:radial-gradient(ellipse at 50% 70%,rgba(140,120,95,.55),rgba(20,18,16,.2) 70%)}
.topbar{position:relative;height:26px;background:rgba(0,0,0,.45);display:flex;align-items:center;justify-content:space-between;padding:0 120px}
.brand{color:var(--orange);font-weight:800;font-size:10px;letter-spacing:.5px}
.nav{display:flex;gap:12px;list-style:none}
.nav li{color:#ddd;font-size:5px;font-weight:600;text-transform:uppercase}
.nav li.active{color:var(--orange)}
.hero-title{position:relative;text-align:center;color:var(--white);font-weight:800;font-size:17px;margin-top:62px;letter-spacing:.3px}
.search{position:relative;width:395px;margin:14px auto 0;background:rgba(0,0,0,.72);padding:10px 14px 14px}
.search h3{color:var(--orange);font-size:8px;font-weight:600;margin-bottom:6px}
.search-grid{display:grid;grid-template-columns:1fr 1fr;gap:8px}
.field{background:var(--white);height:17px;font-size:5px;color:#888;padding:0 6px;display:flex;align-items:center}
.btn{background:var(--orange);color:var(--white);font-weight:700;font-size:6px;height:17px;display:flex;align-items:center;justify-content:center}
.features{display:grid;grid-template-columns:repeat(4,1fr);gap:14px;width:455px;margin:16px auto 0;padding-bottom:18px}
.feature{background:var(--light);height:110px;text-align:center;padding:10px 8px}
.feature-icon{width:30px;height:30px;border-radius:50%;background:var(--orange);margin:0 auto 6px;display:flex;align-items:center;justify-content:center}
.feature h4{color:var(--orange);font-size:5.5px;font-weight:700;margin-bottom:3px}
.feature p{font-size:4.5px;color:#777}
.assets{background:var(--light);padding:20px 0 14px;text-align:center}
.section-title{font-size:11px;font-weight:700;color:#333;letter-spacing:.2px}
.section-sub{font-size:5px;color:#888;margin-top:3px}
.asset-grid{display:grid;grid-template-columns:repeat(4,1fr);gap:3px;width:455px;margin:14px auto 0}
.asset{position:relative;height:100px}
.asset-label{position:absolute;left:0;bottom:0;background:var(--orange);color:var(--white);font-size:4.5px;font-weight:700;padding:3px 6px;text-transform:uppercase}
.a1{background:linear-gradient(135deg,#6b4a3a,#b98a5e)}
.a2{background:linear-gradient(135deg,#3a6a8a,#c8508a)}
.a3{background:linear-gradient(135deg,#2d4a2a,#c7b07a)}
.a4{background:linear-gradient(135deg,#c44a4a,#4a6ac4)}
.a5{background:linear-gradient(135deg,#9a9a9a,#4a4a4a)}
.a6{background:linear-gradient(135deg,#7a7f86,#b0a59a)}
.a7{background:linear-gradient(135deg,#8a2a6a,#3a8a6a)}
.a8{background:linear-gradient(135deg,#5a3a22,#a47040)}
.pager{display:flex;gap:3px;justify-content:center;margin-top:14px}
.pager span{width:10px;height:10px;background:var(--white);border:1px solid var(--grey);font-size:5px;display:flex;align-items:center;justify-content:center;color:#666}
.testimonials{padding:38px 0 22px;text-align:center}
.testi-grid{display:grid;grid-template-columns:1fr 1fr;gap:28px;width:455px;margin:22px auto 0;text-align:left}
.testi{display:flex;gap:8px}
.testi-media{width:28px;flex:none}
.testi-photo{height:28px;background:linear-gradient(#c9c2ba,#8d857d)}
.testi-play{height:16px;background:var(--dark);display:flex;align-items:center;justify-content:center;margin-top:10px}
.testi p{font-size:4.5px;color:#777}
.testi .author{color:var(--orange);font-weight:700;margin-top:4px}
.help{background:var(--orange);height:202px;padding-top:40px;text-align:center}
.help h2{color:var(--white);font-size:9px;font-weight:700;letter-spacing:.3px}
.help-grid{display:grid;grid-template-columns:repeat(3,1fr);gap:28px;width:455px;margin:26px auto 0}
.help-card{background:var(--white);height:96px;display:flex;flex-direction:column;align-items:center;justify-content:center;gap:4px;color:#333}
.help-card .small{font-size:5px}
.help-card .phone{font-size:12px;font-weight:600}
.help-card .label{font-size:8px}
.footer{background:var(--dark);height:110px;color:#999;padding:10px 120px 0;display:grid;grid-template-columns:1.3fr .9fr 1fr;gap:16px;position:relative}
.footer h5{color:var(--white);font-size:5px;font-weight:700;margin-bottom:4px}
.footer p,.footer li{font-size:4.3px;list-style:none}
.footer-links{display:grid;grid-template-columns:1fr 1fr;gap:0 8px}
.footer-mark{position:absolute;right:120px;bottom:26px;color:#3a3a3a;font-weight:800;font-size:12px}
</style>
</head>
<body>
<header class="hero">
  <div class="hero-photo" role="img" aria-label="Photo d'une place pavée en ville au crépuscule"></div>
  <div class="topbar">
    <div class="brand">LOGO</div>
    <ul class="nav">
      <li class="active">Accueil</li><li>Les biens</li><li>Estimation</li><li>FAQ</li><li>Nous contacter</li>
    </ul>
  </div>
  <h1 class="hero-title">ON SE LASSE DE TOUT, SAUF DE L'ARGENT.</h1>
  <form class="search">
    <h3>Nature De L'objet</h3>
    <div class="search-grid">
      <div class="field">Sélectionnez</div>
      <div class="field">Date de l'achat souhaitée</div>
      <div class="field">Prix souhaité</div>
      <div class="btn">RECHERCHER</div>
    </div>
  </form>
</header>

<section class="features">
  <div class="feature">
    <div class="feature-icon"><svg width="16" height="16" viewBox="0 0 16 16"><circle cx="7" cy="7" r="4.5" fill="none" stroke="#fff" stroke-width="1.6"/><line x1="10.5" y1="10.5" x2="14" y2="14" stroke="#fff" stroke-width="1.8"/></svg></div>
    <h4>ESTIMATION</h4>
    <p>Nos experts évaluent votre bien de luxe rapidement et gratuitement, en toute discrétion.</p>
  </div>
  <div class="feature">
    <div class="feature-icon"><svg width="16" height="16" viewBox="0 0 16 16"><rect x="2" y="4" width="12" height="8" fill="none" stroke="#fff" stroke-width="1.5"/><circle cx="8" cy="8" r="2" fill="#fff"/></svg></div>
    <h4>PAIEMENT</h4>
    <p>Recevez les fonds sous quarante-huit heures après accord sur le montant du prêt.</p>
  </div>
  <div class="feature">
    <div class="feature-icon"><svg width="16" height="16" viewBox="0 0 16 16"><path d="M3 8a5 5 0 0 1 9-3M13 8a5 5 0 0 1-9 3" fill="none" stroke="#fff" stroke-width="1.5"/><path d="M12 2v3h-3M4 14v-3h3" fill="none" stroke="#fff" stroke-width="1.5"/></svg></div>
    <h4>RÉCUPÉRATION</h4>
    <p>Remboursez votre prêt et récupérez votre objet assuré, dans son état d'origine.</p>
  </div>
  <div class="feature">
    <div class="feature-icon"><svg width="16" height="16" viewBox="0 0 16 16"><path d="M2 9l4 3 8-8" fill="none" stroke="#fff" stroke-width="1.8"/></svg></div>
    <h4>RACHAT</h4>
    <p>Vous pouvez aussi choisir de nous céder votre bien au meilleur prix du marché.</p>
  </div>
</section>

<section class="assets">
  <h2 class="section-title">LES BIENS QUE NOUS ACCEPTIONS</h2>
  <p class="section-sub">Nous acceptons une large gamme d'objets de valeur, estimés par des spécialistes reconnus.</p>
  <div class="asset-grid">
    <div class="asset a1" role="img" aria-label="Photo d'un masque d'art tribal"><span class="asset-label">Art tribal</span></div>
    <div class="asset a2" role="img" aria-label="Photo d'une peinture colorée"><span class="asset-label">Oeuvres des arts</span></div>
    <div class="asset a3" role="img" aria-label="Photo de bouteilles de vin"><span class="asset-label">Vins &amp; spiritueux</span></div>
    <div class="asset a4" role="img" aria-label="Photo d'une oeuvre d'art contemporain"><span class="asset-label">Art contemporain</span></div>
    <div class="asset a5" role="img" aria-label="Photo d'une montre de luxe"><span class="asset-label">Montres</span></div>
    <div class="asset a6" role="img" aria-label="Photo d'un parc de voitures"><span class="asset-label">Voitures</span></div>
    <div class="asset a7" role="img" aria-label="Photo de pierres précieuses"><span class="asset-label">Pierres précieuses</span></div>
    <div class="asset a8" role="img" aria-label="Photo d'un sac en cuir"><span class="asset-label">Maroquinerie</span></div>
  </div>
  <div class="pager"><span>‹</span><span>›</span></div>
</section>

<section class="testimonials">
  <h2 class="section-title">DERNIERS&nbsp; TEMOIGNAGES</h2>
  <div class="testi-grid">
    <article class="testi">
      <div class="testi-media">
        <div class="testi-photo" role="img" aria-label="Portrait d'un client"></div>
        <div class="testi-play"><svg width="6" height="7" viewBox="0 0 6 7"><path d="M0 0l6 3.5L0 7z" fill="#fff"/></svg></div>
      </div>
      <div>
        <p>Service rapide et très professionnel. J'ai obtenu un prêt contre ma montre en deux jours seulement, sans démarches compliquées. L'équipe a été à l'écoute du début à la fin et l'objet m'a été rendu en parfait état. Je recommande vivement cette solution.</p>
        <p class="author">Julien M.</p>
      </div>
    </article>
    <article class="testi">
      <div class="testi-media">
        <div class="testi-photo" role="img" aria-label="Portrait d'une cliente"></div>
        <div class="testi-play"><svg width="6" height="7" viewBox="0 0 6 7"><path d="M0 0l6 3.5L0 7z" fill="#fff"/></svg></div>
      </div>
      <div>
        <p>Une estimation juste et transparente de mes bijoux. Les conditions étaient claires et les fonds sont arrivés très vite sur mon compte. Une vraie alternative au crédit bancaire classique, avec discrétion et sérieux. Merci à toute l'équipe pour son accompagnement.</p>
        <p class="author">Claire D.</p>
      </div>
    </article>
  </div>
</section>

<section class="help">
  <h2>BESOIN D'AIDE? NOUS SOMMES A VOTRE ECOUTE</h2>
  <div class="help-grid">
    <div class="help-card">
      <svg width="22" height="18" viewBox="0 0 22 18"><path d="M2 6c0-3 4-4 9-4s9 1 9 4l-3 1-1-2H6L5 7z" fill="#222"/><rect x="5" y="8" width="12" height="9" rx="2" fill="#222"/><circle cx="11" cy="12.5" r="2.2" fill="#fff"/></svg>
      <span class="small">Du lundi au vendredi de 9h à 19h</span>
      <span class="phone">01 23 45 67 89</span>
    </div>
    <div class="help-card">
      <svg width="24" height="20" viewBox="0 0 24 20"><path d="M2 2h20v12H10l-5 4v-4H2z" fill="none" stroke="#222" stroke-width="1.8"/><text x="12" y="11" font-family="Open Sans,sans-serif" font-size="6" font-weight="700" text-anchor="middle" fill="#222">FAQ</text></svg>
      <span class="label">Question Frequentes</span>
    </div>
    <div class="help-card">
      <svg width="22" height="16" viewBox="0 0 22 16"><rect x="1" y="1" width="20" height="14" fill="#222"/><path d="M1 1l10 8 10-8" fill="none" stroke="#fff" stroke-width="1.4"/></svg>
      <span class="small">Formulaire de contact</span>
      <span class="small">contact@enterprise-pret.fr</span>
    </div>
  </div>
</section>

<footer class="footer">
  <div>
    <h5>RÉSERVEZ EN VUE DE PRÊTER</h5>
    <p>Nous proposons des prêts garantis par vos objets de luxe, estimés par des experts indépendants. Vos biens sont conservés en lieu sûr et assurés pendant toute la durée du contrat jusqu'au remboursement.</p>
  </div>
  <div>
    <h5>COMPANY</h5>
    <ul class="footer-links">
      <li>Accueil</li><li>Nos biens</li><li>Estimation</li><li>Nos experts</li><li>Les biens</li><li>Mentions</li><li>FAQ</li><li>Presse</li><li>Nous contacter</li>
    </ul>
  </div>
  <div>
    <h5>CONTACT US</h5>
    <ul>
      <li>12 rue des Lilas</li><li>75011 Paris, France</li><li>Du lundi au vendredi</li><li>01 23 45 67 89</li><li>contact@enterprise-pret.fr</li>
    </ul>
  </div>
  <div class="footer-mark">LOGO</div>
</footer>
</body>
</html>
```